Brisa Pastry Mill Business card

We are empanada whole-sellers and I want a business card design with a picture of an empanada on it that also mentions first trial order FREE. our contact number 555-214-7093 our website www.brisapastry.example and business email Tobin@brisapastry.example

If you want any of our artwork please feel free to email me at the address above.

```html
<!DOCTYPE html>
<html lang="en">
<head>
<meta charset="utf-8">
<title>Brisa Pastry Mill – Business Card</title>
<link rel="stylesheet" href="https://fonts.googleapis.com/css2?family=Oswald:wght@400&family=Roboto+Slab:wght@800&family=Open+Sans:wght@300&display=swap">
<style>
  :root {
    --stage: #ecebe8;
    --card-white: #ffffff;
    --ink: #1b1b1b;
    --gold-top: #eeae25;
    --gold-bottom: #d99a1c;
    --band-brown: #5e3b1c;
    --accent-yellow: #fff200;
    --icon-brown: #8a6a45;
    --pastry-light: #ecd2a0;
    --pastry-dark: #c6904f;
  }
  * { box-sizing: border-box; margin: 0; padding: 0; }
  html, body { width: 1200px; height: 1024px; overflow: hidden; }
  body {
    background: var(--stage);
    display: flex;
    flex-direction: column;
    align-items: center;
    justify-content: center;
    gap: 32px;
  }
  .card {
    position: relative;
    width: 880px;
    height: 480px;
    overflow: hidden;
    box-shadow: 0 6px 18px rgba(0,0,0,0.18);
  }
  .card--front { background: var(--card-white); }
  .card--back { background: linear-gradient(160deg, var(--gold-top), var(--gold-bottom)); }

  .brand-name {
    font-family: "Roboto Slab", Georgia, serif;
    font-weight: 800;
    color: var(--ink);
    line-height: 1;
    white-space: nowrap;
  }
  .brand-tagline {
    font-family: "Roboto Slab", Georgia, serif;
    font-weight: 800;
    color: var(--ink);
    text-transform: uppercase;
    letter-spacing: 0.5px;
    white-space: nowrap;
  }

  /* front */
  .card--front .brand {
    position: absolute;
    left: 56px;
    top: 70px;
  }
  .card--front .brand-name { font-size: 50px; }
  .card--front .brand-tagline { font-size: 17px; margin-top: 12px; }

  .product-photo {
    position: absolute;
    left: 90px;
    top: 210px;
    width: 300px;
    height: 210px;
    border-radius: 46% 54% 50% 50% / 55% 50% 50% 45%;
    background: radial-gradient(ellipse at 40% 40%, var(--pastry-light), var(--pastry-dark));
  }

  .contact-list {
    position: absolute;
    left: 560px;
    top: 80px;
    list-style: none;
    display: flex;
    flex-direction: column;
    gap: 22px;
  }
  .contact-item {
    display: flex;
    align-items: center;
    gap: 16px;
    font-family: "Open Sans", Arial, sans-serif;
    font-weight: 300;
    font-size: 19px;
    color: #333;
  }
  .contact-icon { width: 22px; height: 22px; flex: none; }

  /* back */
  .card--back .brand {
    position: absolute;
    left: 0; right: 0;
    top: 86px;
    text-align: center;
  }
  .card--back .brand-name { font-size: 72px; }
  .card--back .brand-tagline { font-size: 21px; margin-top: 18px; }

  .offer-band {
    position: absolute;
    left: 0; right: 0;
    top: 318px;
    height: 82px;
    background: var(--band-brown);
    display: flex;
    align-items: center;
    padding-left: 60px;
  }
  .offer-text {
    font-family: "Oswald", "Arial Narrow", sans-serif;
    font-weight: 400;
    font-size: 36px;
    color: #ffffff;
    letter-spacing: 0.5px;
  }
  .offer-text .offer-free { color: var(--accent-yellow); }
</style>
</head>
<body>

  <section class="card card--front" aria-label="Business card front">
    <div class="brand">
      <div class="brand-name">Brisa Pastry Mill</div>
      <div class="brand-tagline">Malaysian &amp; Thai Street Food</div>
    </div>

    <div class="product-photo" role="img" aria-label="Photo of three golden baked empanadas"></div>

    <ul class="contact-list">
      <li class="contact-item">
        <svg class="contact-icon" viewBox="0 0 22 22" aria-hidden="true">
          <circle cx="11" cy="11" r="11" fill="var(--icon-brown)"/>
          <path d="M7.5 5.5 L9.5 5.5 L10.3 8.2 L9 9.2 Q10.3 11.9 12.8 13 L13.8 11.7 L16.5 12.5 L16.5 14.5 Q16 16.5 13.5 16 Q7 14 6 8 Q6 5.8 7.5 5.5 Z" fill="#fff"/>
        </svg>
        555-214-7093
      </li>
      <li class="contact-item">
        <svg class="contact-icon" viewBox="0 0 22 22" aria-hidden="true">
          <circle cx="11" cy="11" r="11" fill="var(--icon-brown)"/>
          <rect x="5.5" y="7" width="11" height="8" fill="none" stroke="#fff" stroke-width="1.4"/>
          <path d="M5.5 7 L11 11.5 L16.5 7" fill="none" stroke="#fff" stroke-width="1.4"/>
        </svg>
        Tobin@brisapastry.example
      </li>
      <li class="contact-item">
        <svg class="contact-icon" viewBox="0 0 22 22" aria-hidden="true">
          <circle cx="11" cy="11" r="11" fill="var(--icon-brown)"/>
          <circle cx="11" cy="11" r="6" fill="none" stroke="#fff" stroke-width="1.3"/>
          <ellipse cx="11" cy="11" rx="2.6" ry="6" fill="none" stroke="#fff" stroke-width="1.1"/>
          <line x1="5" y1="11" x2="17" y2="11" stroke="#fff" stroke-width="1.1"/>
        </svg>
        www.brisapastry.example
      </li>
    </ul>
  </section>

  <section class="card card--back" aria-label="Business card back">
    <div class="brand">
      <div class="brand-name">Brisa Pastry Mill</div>
      <div class="brand-tagline">Malaysian &amp; Thai Street Food</div>
    </div>
    <div class="offer-band">
      <p class="offer-text">First Trial Order <span class="offer-free">FREE</span></p>
    </div>
  </section>

</body>
</html>
```